Professional & attention grabbing.

A business card design, front and back. I already have a logo I will attach, but I am open to something new as well.
Things to include:
Name:
Title:
Phone:
Email:
Wanting something that is professional but attention grabbing.
Also we do a lot of work using drones on natural gas pipelines (leading the future)if you want to include any of that. I'm open to ideas.
Target Market(s)
Natural gas transmission industry / greenhouse gas mitigation industry
Industry/Entity Type
Business
Contact Information for Business Card
All details have been conveyed above.
Colors
Designer to choose colors to be used in the design.
Look and feel
Each slider illustrates characteristics of the customer's brand and the style your logo design should communicate.

```html
<!DOCTYPE html>
<html lang="en">
<head>
<meta charset="utf-8">
<title>Ridgeline Survey Works – Business Card</title>
<link rel="stylesheet" href="https://fonts.googleapis.com/css2?family=Exo+2:wght@500;700;800&family=Open+Sans:wght@400;600&display=swap">
<style>
  :root {
    --bg: #e9e9eb;
    --card: #ffffff;
    --red: #c8202a;
    --ink: #2b2b2d;
    --muted: #4a4a4d;
    --rule-grey: #cfcfd2;
    --sunset-top: #c9b8a4;
    --sunset-bottom: #4f5662;
    --site-top: #b9c9de;
    --site-bottom: #8a7b68;
    --water-top: #3f9cc6;
    --water-bottom: #1d6b8f;
    --grass: #4f7a45;
  }
  * { box-sizing: border-box; margin: 0; padding: 0; }
  html, body { width: 1200px; height: 900px; overflow: hidden; }
  body {
    background: var(--bg);
    font-family: "Open Sans", Arial, sans-serif;
    color: var(--ink);
    position: relative;
  }
  .card {
    position: absolute;
    top: 295px;
    width: 540px;
    height: 310px;
    border-radius: 22px;
    overflow: hidden;
    background: var(--card);
    box-shadow: 0 6px 20px rgba(0,0,0,.18);
  }
  .card--front { left: 40px; }
  .card--back { left: 620px; }

  /* Front */
  .brand {
    position: absolute;
    top: 40px;
    right: 40px;
    display: flex;
    align-items: center;
    gap: 10px;
  }
  .brand__mark { width: 22px; height: 22px; background: var(--red); }
  .brand__name {
    font-family: "Exo 2", Arial, sans-serif;
    font-weight: 800;
    font-size: 24px;
    color: var(--ink);
    letter-spacing: .5px;
  }
  .rule-red {
    position: absolute;
    left: 34px; right: 34px;
    top: 168px;
    height: 1.5px;
    background: var(--red);
  }
  .person {
    position: absolute;
    left: 34px;
    top: 180px;
  }
  .person__name {
    font-family: "Exo 2", Arial, sans-serif;
    font-weight: 800;
    font-size: 22px;
    color: var(--red);
    letter-spacing: .5px;
    line-height: 1;
  }
  .person__title {
    font-family: "Exo 2", Arial, sans-serif;
    font-weight: 700;
    font-size: 15px;
    color: var(--muted);
    margin-top: 4px;
    letter-spacing: .5px;
  }
  .rule-grey {
    position: absolute;
    left: 34px;
    width: 210px;
    top: 232px;
    height: 1px;
    background: var(--rule-grey);
  }
  .contacts {
    position: absolute;
    left: 34px;
    top: 242px;
    list-style: none;
    font-size: 14px;
    color: var(--muted);
  }
  .contacts li { display: flex; align-items: center; gap: 9px; height: 24px; }
  .contacts svg { width: 14px; height: 14px; flex: none; }
  .address {
    position: absolute;
    right: 34px;
    top: 178px;
    text-align: right;
    font-size: 13.5px;
    line-height: 1.4;
    color: var(--muted);
  }

  /* Back */
  .photo { position: absolute; }
  .photo--pipeline {
    left: 0; top: 0; width: 280px; height: 158px;
    background: linear-gradient(180deg, var(--sunset-top), #d9a477 45%, var(--sunset-bottom));
  }
  .photo--site {
    left: 283px; top: 0; width: 257px; height: 158px;
    background: linear-gradient(180deg, var(--site-top), #d7dde6 45%, var(--site-bottom));
  }
  .photo--water {
    left: 0; top: 161px; width: 540px; height: 149px;
    background: linear-gradient(180deg, var(--water-top), var(--water-bottom) 70%, var(--grass));
  }
  .web-band {
    position: absolute;
    left: 150px; right: 0;
    top: 200px;
    height: 26px;
    background: rgba(255,255,255,.85);
    transform: rotate(-4deg);
    transform-origin: right center;
  }
  .website {
    position: absolute;
    right: 40px;
    top: 203px;
    font-size: 14px;
    font-weight: 600;
    color: var(--red);
    transform: rotate(-4deg);
    transform-origin: right center;
  }
</style>
</head>
<body>

<section class="card card--front" aria-label="Business card front">
  <div class="brand">
    <span class="brand__mark"></span>
    <span class="brand__name">Ridgeline Survey Works</span>
  </div>

  <div class="rule-red"></div>

  <div class="person">
    <p class="person__name">DANIEL HARLOW</p>
    <p class="person__title">DIRECTOR</p>
  </div>

  <p class="address">418 Meridian Avenue,<br>Cedar Falls, Osaka</p>

  <div class="rule-grey"></div>

  <ul class="contacts">
    <li>
      <svg viewBox="0 0 14 14" aria-hidden="true"><rect width="14" height="14" rx="2" fill="#c8202a"/><path d="M4 3.5c.6 2.9 2.2 5 5.5 6.5l1-1.3-1.6-1-1 .8c-1-.6-1.8-1.4-2.3-2.4l.8-.9-.9-1.7z" fill="#fff"/></svg>
      <span>555-014-2270</span>
    </li>
    <li>
      <svg viewBox="0 0 14 14" aria-hidden="true"><rect width="14" height="14" rx="2" fill="#c8202a"/><rect x="3" y="4.2" width="8" height="5.6" fill="none" stroke="#fff" stroke-width="1"/><path d="M3 4.4l4 3 4-3" fill="none" stroke="#fff" stroke-width="1"/></svg>
      <span>contact@ridgelinesurvey.com</span>
    </li>
  </ul>
</section>

<section class="card card--back" aria-label="Business card back">
  <div class="photo photo--pipeline" role="img" aria-label="Photo of a drone flying beside an elevated gas pipeline at sunset"></div>
  <div class="photo photo--site" role="img" aria-label="Photo of a drone over a construction site with cranes"></div>
  <div class="photo photo--water" role="img" aria-label="Photo of a drone inspecting a covered blue reservoir"></div>
  <div class="web-band"></div>
  <p class="website">www.ridgelinesurvey.com</p>
</section>

</body>
</html>
```